Kestrel Building Works Business Card and more!

We need a business card design for Kestrel Building Works Ltd, a respected building company that specialises in high quality designer homes.

We're after a sleek, clean, modern business card that incorporates our new logo (see attached) and colours, with black being the background.

We are Certified Framing Guild and need to include their logo (see attached) on our cards, balancing but not taking over our logo.

Details to be included:

Malcolm Tivey
Director

Phone: 0218845126
Email: kestrelbuild.nz@maildrop-example.co.nz
Website: www.kestrelbuildingworks-example.co.nz

Additional Information

A start up website is also under construction and needing attention and letterheads are needed!

We look forward to your designs!

Target Market(s)

30+ people who are interested in building new or renovating current homes

Industry/Entity Type

Construction

Contact Information for Business Card

Malcolm Tivey
Director

Phone: 0218845126
Facebook: www.socialpage-example.com/kestrelbuild.nz

Font styles to use
Serif

Colors

Designer to choose colors to be used in the design.

Requirements
Must have
• Our new logo
• Our colours
• cfg logo

```html
<!DOCTYPE html>
<html lang="en">
<head>
<meta charset="utf-8">
<title>Kestrel Building Works – Business Card</title>
<link rel="stylesheet" href="https://fonts.googleapis.com/css2?family=Cinzel:wght@600&family=EB+Garamond:wght@400&family=Open+Sans:wght@400&display=swap">
<style>
  :root {
    --backdrop: #1c1d21;
    --card: #0b0b0c;
    --gold: #c9975a;
    --gold-soft: #d8a86a;
    --white: #f4f2ee;
    --muted: #d9d9d9;
  }
  * { margin: 0; padding: 0; box-sizing: border-box; }
  html, body { width: 1200px; height: 900px; overflow: hidden; }
  body { background: var(--backdrop); position: relative; }

  .card {
    position: absolute;
    width: 520px;
    height: 300px;
    background: var(--card);
    border-radius: 22px;
    overflow: hidden;
    box-shadow: 0 18px 40px rgba(0,0,0,0.55);
  }
  .card--front { left: 70px; top: 450px; }
  .card--back  { left: 610px; top: 150px; }

  .wordmark {
    font-family: "Cinzel", serif;
    font-weight: 600;
    color: var(--white);
    text-align: center;
    line-height: 1.05;
  }

  /* Front */
  .card--front .wordmark {
    position: absolute;
    left: 0; right: 0; top: 78px;
    font-size: 40px;
    letter-spacing: 4px;
  }
  .brand-band {
    position: absolute;
    left: 0; right: 0; bottom: 0;
    height: 52px;
    background: var(--gold);
    display: flex;
    align-items: center;
    justify-content: center;
  }
  .brand-band .website {
    font-family: "Open Sans", sans-serif;
    font-size: 17px;
    color: #1a1410;
    letter-spacing: 0.3px;
  }

  /* Back */
  .card--back .wordmark {
    position: absolute;
    left: 26px; top: 36px;
    width: 250px;
    font-size: 24px;
    letter-spacing: 2px;
  }
  .contact-list {
    position: absolute;
    left: 28px; top: 138px;
    list-style: none;
    font-family: "Open Sans", sans-serif;
    font-size: 13.5px;
    color: var(--muted);
  }
  .contact-list li { display: flex; align-items: center; gap: 8px; margin-bottom: 6px; }
  .contact-list svg { width: 12px; height: 12px; flex: none; }
  .person {
    position: absolute;
    right: 30px; top: 112px;
    text-align: right;
    font-family: "EB Garamond", serif;
  }
  .person__name { font-size: 27px; color: var(--gold-soft); }
  .person__role { font-size: 20px; color: var(--white); }
  .guild-badge {
    position: absolute;
    right: 34px; bottom: 26px;
    width: 82px; height: 82px;
  }
</style>
</head>
<body>

<section class="card card--front" aria-label="Business card front">
  <div class="wordmark">Kestrel<br>Building Works</div>
  <div class="brand-band">
    <span class="website">www.kestrelbuildingworks-example.co.nz</span>
  </div>
</section>

<section class="card card--back" aria-label="Business card back">
  <div class="wordmark">Kestrel<br>Building Works</div>

  <ul class="contact-list">
    <li>
      <svg viewBox="0 0 12 12" aria-hidden="true"><path fill="#d8a86a" d="M2.5 1h2l1 3-1.3 1a6 6 0 0 0 2.8 2.8L8 6.5l3 1v2A1.5 1.5 0 0 1 9.5 11 8.5 8.5 0 0 1 1 2.5 1.5 1.5 0 0 1 2.5 1z"/></svg>
      021 884 5126
    </li>
    <li>
      <svg viewBox="0 0 12 12" aria-hidden="true"><rect x="0.5" y="2" width="11" height="8" rx="1" fill="#d8a86a"/><path d="M1 2.8l5 3.6 5-3.6" stroke="#0b0b0c" stroke-width="1" fill="none"/></svg>
      kestrelbuild.nz@maildrop-example.co.nz
    </li>
    <li>
      <svg viewBox="0 0 12 12" aria-hidden="true"><circle cx="6" cy="6" r="5.5" fill="#d8a86a"/></svg>
      kestrelbuild.nz
    </li>
  </ul>

  <div class="person">
    <div class="person__name">Malcolm Tivey</div>
    <div class="person__role">Director</div>
  </div>

  <svg class="guild-badge" viewBox="0 0 82 82" role="img" aria-label="Certified Framing Guild badge">
    <circle cx="41" cy="41" r="40" fill="var(--white)"/>
    <circle cx="41" cy="41" r="27" fill="var(--card)"/>
  </svg>
</section>

</body>
</html>
```